"Nail Care" Postcard

Hello,

We are looking to redesign our current post card. The target audience of this post card age is 50+. We will be mailing these postcards through Tamblo Cards.
The goal of the message is to remind them that it is time to get their (toe) nail care done.

Attached is our previous postcard.
Post card size: 4.2” x 5.5”
Backside of the postcards needs space for the mailing address and postage.
Our address and logo need to be present.
The message of the back of the postcard needs to be present as well.
Examples of stock images must come with the example.
Files preferred to be in TIFF or .ai

Thank you,
Dorian F.

```html
<!DOCTYPE html>
<html lang="en">
<head>
<meta charset="utf-8">
<title>Hartwell Foot &amp; Ankle – Nail Care Postcard</title>
<link rel="stylesheet" href="https://fonts.googleapis.com/css2?family=Fira+Sans+Condensed:ital,wght@0,500;0,600;0,700;1,600&family=Noto+Serif:wght@400&display=swap">
<style>
  :root {
    --stage: #8f8f8f;
    --paper: #ffffff;
    --orange: #f0804c;
    --orange-soft: #f6a27a;
    --teal: #57c0a5;
    --teal-bright: #3dffd0;
    --teal-deep: #1b8f72;
    --ink: #222222;
    --night: #151515;
    --mail-zone: #e0e0e0;
    --skin-light: #f6ddd0;
    --skin-mid: #e9bfa9;
    --glove: #3f63d8;
  }
  * { margin: 0; padding: 0; box-sizing: border-box; }
  html, body { width: 1040px; height: 1200px; overflow: hidden; background: var(--stage); }
  body { position: relative; font-family: "Fira Sans Condensed", "Arial Narrow", sans-serif; }

  .postcard {
    position: absolute; left: 236px; width: 577px; height: 441px;
    background: var(--paper); overflow: hidden;
    box-shadow: 0 2px 4px rgba(0,0,0,.35);
  }
  .postcard--front { top: 131px; }
  .postcard--back { top: 645px; }
  .postcard svg.backdrop { position: absolute; inset: 0; }

  .brand { position: absolute; display: flex; align-items: center; gap: 6px; }
  .brand__mark { width: 16px; height: 16px; background: var(--teal); }
  .brand__name { color: var(--orange); font-weight: 700; line-height: .95; text-align: right; text-transform: uppercase; }

  .front .brand { right: 26px; top: 34px; }
  .front .brand__name { font-size: 21px; }
  .front .brand__mark { width: 20px; height: 20px; }

  .tagline-pill {
    position: absolute; left: 392px; top: 106px; width: 160px; height: 24px;
    background: var(--teal); color: #fff; border-radius: 12px 0 0 12px;
    font-size: 14px; font-weight: 600; line-height: 24px; text-align: right; padding-right: 7px;
  }
  .tagline-pill em { font-style: italic; }

  .headline { position: absolute; right: 25px; top: 135px; text-align: right; font-weight: 600; line-height: 1; text-transform: uppercase; }
  .headline span { display: block; }
  .headline .hl-orange { color: var(--orange); font-size: 28px; }
  .headline .hl-big { color: var(--orange); font-size: 47px; font-weight: 700; line-height: .9; }
  .headline .hl-teal { color: var(--teal); font-size: 28px; }

  .result { position: absolute; top: 271px; width: 98px; height: 90px; border: 1px solid var(--teal-bright); }
  .result .photo { position: absolute; inset: 2px; background: linear-gradient(180deg, #fbf3ee 0%, var(--skin-light) 40%, var(--skin-mid) 100%); }
  .result .label { position: absolute; bottom: 5px; width: 100%; text-align: center; color: #8a4a1e; font-size: 11px; font-weight: 700; letter-spacing: .5px; }
  .result--before { left: 348px; }
  .result--after { left: 452px; }

  .front-phone { position: absolute; right: 27px; top: 374px; color: var(--orange); font-size: 28px; font-weight: 600; line-height: 1; }
  .front-web { position: absolute; right: 27px; top: 403px; color: var(--teal); font-size: 17px; font-weight: 600; line-height: 1; }

  .back .brand { left: 31px; top: 27px; }
  .back .brand__name { font-size: 13px; }
  .back .brand__mark { width: 14px; height: 14px; }
  .address { position: absolute; left: 31px; top: 66px; font-family: "Noto Serif", Georgia, serif; font-size: 11.5px; line-height: 14.5px; color: var(--ink); }

  .motto { position: absolute; left: 262px; top: 32px; color: var(--orange); font-weight: 700; text-transform: uppercase; line-height: 1; }
  .motto span { display: block; }
  .motto .m-top { font-size: 40px; letter-spacing: .5px; }
  .motto .m-bottom { font-size: 28px; }

  .reminder { position: absolute; left: 29px; top: 139px; color: var(--orange); font-size: 21.5px; font-weight: 500; line-height: 22px; text-transform: uppercase; }
  .call { position: absolute; left: 31px; top: 237px; color: var(--teal); font-size: 15.5px; font-weight: 500; line-height: 16px; }
  .back-phone { position: absolute; left: 29px; top: 270px; color: var(--teal-deep); font-size: 31px; font-weight: 600; line-height: 1; letter-spacing: .5px; }
  .disclaimer { position: absolute; left: 32px; top: 318px; color: #555; font-size: 9px; font-weight: 500; line-height: 11px; }
</style>
</head>
<body>

<section class="postcard postcard--front front" aria-label="Postcard front">
  <svg class="backdrop" width="577" height="441" viewBox="0 0 577 441">
    <defs>
      <linearGradient id="treatmentTone" x1="0" y1="0" x2="1" y2="1">
        <stop offset="0" stop-color="#f4f4f6"/>
        <stop offset=".45" stop-color="var(--skin-light)"/>
        <stop offset=".75" stop-color="#c9cde2"/>
        <stop offset="1" stop-color="var(--glove)"/>
      </linearGradient>
    </defs>
    <path d="M204 0 C 320 40, 348 200, 320 300 C 305 360, 285 410, 268 441 L 253 441 C 300 360, 340 220, 295 110 C 275 60, 245 25, 204 0 Z" fill="var(--orange)"/>
    <path d="M240 0 C 300 70, 315 180, 300 280 C 292 340, 275 400, 258 441 L 248 441 C 290 360, 318 220, 285 110 C 272 60, 258 25, 240 0 Z" fill="var(--orange-soft)"/>
    <path d="M210 441 C 275 400, 320 320, 322 230 C 323 160, 300 80, 255 30 C 305 80, 335 160, 330 240 C 326 330, 290 400, 253 441 Z" fill="var(--teal)"/>
    <path d="M240 441 C 290 400, 325 320, 330 240 C 333 170, 315 90, 270 40 C 322 100, 345 170, 340 250 C 335 330, 300 400, 262 441 Z" fill="var(--teal-bright)"/>
    <path d="M0 0 L204 0 C 270 45, 300 120, 300 210 C 300 310, 260 390, 201 441 L0 441 Z" fill="url(#treatmentTone)" role="img" aria-label="Photo: gloved podiatrist hands filing the toenails of a bare foot with an electric nail drill"/>
  </svg>

  <div class="brand">
    <span class="brand__mark"></span>
    <span class="brand__name">Hartwell<br>Foot &amp; Ankle</span>
  </div>

  <div class="tagline-pill">We Keep <em>You Moving</em></div>

  <h1 class="headline">
    <span class="hl-orange">Have your</span>
    <span class="hl-big">Nails</span>
    <span class="hl-teal">Been taken</span>
    <span class="hl-teal">care of?</span>
  </h1>

  <div class="result result--before">
    <div class="photo" role="img" aria-label="Photo: toes with a discoloured big toenail before treatment"></div>
    <span class="label">BEFORE</span>
  </div>
  <div class="result result--after">
    <div class="photo" role="img" aria-label="Photo: the same toes with clean, healthy nails after treatment"></div>
    <span class="label">AFTER</span>
  </div>

  <div class="front-phone">555-014-2290</div>
  <div class="front-web">WWW.HARTWELLFEET.COM</div>
</section>

<section class="postcard postcard--back back" aria-label="Postcard back">
  <svg class="backdrop" width="577" height="441" viewBox="0 0 577 441">
    <path d="M206 0 L577 0 L577 441 L70 441 L70 368 L291 368 L291 137 L300 137 C 260 110, 225 60, 206 0 Z" fill="var(--night)"/>
    <path d="M450 0 L577 0 L577 137 L450 137 Z M291 137 L577 137 L577 441 L70 441 L70 368 L291 368 Z" fill="var(--mail-zone)"/>
    <path d="M162 0 L180 0 C 205 75, 245 135, 291 163 L291 173 C 230 140, 185 80, 162 0 Z" fill="var(--orange)"/>
    <path d="M190 0 L200 0 C 215 60, 250 110, 291 140 L291 158 C 245 125, 208 70, 190 0 Z" fill="var(--teal)"/>
    <path d="M200 0 L206 0 C 222 60, 255 105, 291 130 L291 140 C 250 110, 215 60, 200 0 Z" fill="var(--teal-bright)"/>
  </svg>

  <div class="brand">
    <span class="brand__mark"></span>
    <span class="brand__name">Hartwell<br>Foot &amp; Ankle</span>
  </div>
  <address class="address" style="font-style:normal">58 Larkspur Ave.<br>Ste. 210<br>Brookhaven, MD 21990</address>

  <div class="motto">
    <span class="m-top">We Keep</span>
    <span class="m-bottom">You Moving</span>
  </div>

  <h2 class="reminder">We are pleased<br>to inform you may<br>be due for your<br>bimonthly nail care!</h2>
  <p class="call">Please call our office<br>to schedule your appointment.</p>
  <p class="back-phone">(555)014-2290</p>
  <p class="disclaimer">*if you have received nail card within the past<br>two months, please disregard*</p>
</section>

</body>
</html>
```